IT Consulting company Needs a Logo Design and Business Cards

I need a New Logo and Business Cards for an established IT Managed Services Company that specializes in flat-rate managed IT services. We provide Design and Build, Help Desk, Onsite and Remote Support Services.

Target Market(s)

Corporate Clients

Industry/Entity Type

It Company

Logo Text

Halvern Systems Collective

Requirements
Nice to have
• Tag Line= Technology at Lightning Speed

```html
<!DOCTYPE html>
<html lang="en">
<head>
<meta charset="utf-8">
<title>Halvern Systems Collective – Business Cards</title>
<link rel="stylesheet" href="https://fonts.googleapis.com/css2?family=Open+Sans:wght@400;600&display=swap">
<style>
  :root {
    --page-bg: #e9e7e4;
    --card-dark: #0b0b0b;
    --card-light: #ffffff;
    --brand-blue: #3a9ddb;
    --brand-grey: #8c8c8c;
    --text-grey: #6f6f6f;
    --tagline-grey: #9a9a9a;
  }
  * { margin: 0; padding: 0; box-sizing: border-box; }
  html, body { width: 1200px; height: 900px; overflow: hidden; }
  body {
    background: var(--page-bg);
    font-family: "Open Sans", Arial, sans-serif;
    display: flex;
    flex-direction: column;
    align-items: center;
    justify-content: center;
    gap: 40px;
  }
  .card {
    width: 700px;
    height: 400px;
    box-shadow: 0 10px 30px rgba(0,0,0,0.18);
    position: relative;
  }
  .card--back {
    background: radial-gradient(ellipse at 60% 45%, #1e1e1e 0%, var(--card-dark) 70%);
    display: flex;
    flex-direction: column;
    align-items: center;
    justify-content: center;
    gap: 34px;
  }
  .card--front {
    background: var(--card-light);
    display: flex;
    align-items: center;
    padding: 0 50px;
  }
  .brand-name {
    display: flex;
    align-items: center;
    gap: 12px;
    color: var(--brand-blue);
    font-weight: 600;
    line-height: 1.1;
  }
  .brand-name__mark {
    width: 22px;
    height: 22px;
    background: var(--brand-blue);
    flex: none;
  }
  .card--back .brand-name { font-size: 34px; }
  .tagline {
    color: var(--tagline-grey);
    font-size: 20px;
    letter-spacing: 0.5px;
  }
  .card--front .brand-name {
    font-size: 25px;
    width: 270px;
  }
  .divider {
    width: 2px;
    height: 190px;
    background: var(--brand-blue);
    margin: 0 36px 0 30px;
    flex: none;
  }
  .contact { color: var(--text-grey); }
  .contact__name {
    font-size: 27px;
    color: var(--text-grey);
    letter-spacing: 0.5px;
    line-height: 1.1;
  }
  .contact__role {
    font-size: 17px;
    color: var(--brand-blue);
    letter-spacing: 1px;
    margin-bottom: 18px;
  }
  .contact__list { list-style: none; }
  .contact__item {
    display: flex;
    align-items: center;
    gap: 10px;
    font-size: 18px;
    line-height: 1.7;
  }
  .contact__icon { width: 16px; height: 16px; flex: none; }
  .contact__address { font-size: 18px; margin-top: 4px; }
</style>
</head>
<body>
  <section class="card card--back">
    <div class="brand-name"><span class="brand-name__mark"></span>Halvern Systems Collective</div>
    <p class="tagline">Technology at Lightning Speed</p>
  </section>

  <section class="card card--front">
    <div class="brand-name"><span class="brand-name__mark"></span>Halvern Systems Collective</div>
    <div class="divider"></div>
    <div class="contact">
      <h1 class="contact__name">YOUR NAME</h1>
      <p class="contact__role">Owner</p>
      <ul class="contact__list">
        <li class="contact__item">
          <svg class="contact__icon" viewBox="0 0 16 16"><path d="M4 1 L6.5 1 L7 5 L5.5 6 C6.3 8 8 9.7 10 10.5 L11 9 L15 9.5 L15 12 C15 13.5 13.5 15 12 15 C6 14.5 1.5 10 1 4 C1 2.5 2.5 1 4 1 Z" fill="#3a9ddb"/></svg>
          000 000 0000
        </li>
        <li class="contact__item">
          <svg class="contact__icon" viewBox="0 0 16 16"><rect x="1" y="3" width="14" height="10" fill="#3a9ddb"/><path d="M1.5 3.5 L8 9 L14.5 3.5" fill="none" stroke="#fff" stroke-width="1.2"/></svg>
          youremail@xyz.com
        </li>
        <li class="contact__item">
          <svg class="contact__icon" viewBox="0 0 16 16" fill="none" stroke="#3a9ddb" stroke-width="1.2"><circle cx="8" cy="8" r="6.5"/><ellipse cx="8" cy="8" rx="3" ry="6.5"/><path d="M1.5 8 H14.5 M2.5 5 H13.5 M2.5 11 H13.5"/></svg>
          www.yourwebsite.com
        </li>
      </ul>
      <p class="contact__address">Your Address here</p>
    </div>
  </section>
</body>
</html>
```